Flyer-Design für Wechseljahresberatung
Zielgruppe
Zielgruppe: überwiegend Frauen
psycholog. Beratung in allen Lebenslagen, Wechseljahresberatung , Gesundheits- und Ernährungsberatung, Fastenbegleitung, Trauerbegleitung, Bachblütenberatung,Klangmassagen
Aufgabenstellung
es geht um einen 6teiligen Kurs für Frauen zwischen Ende 30 bis Ende 60. Beginn der Wechseljahre , Leben in den Wechseljahren und was kommt danach? Wie erkennt man (Frau) körperl. oder seelische Probleme, die schon auf We.jahre hindeuten? Wie gehe Frau damit um? Was passiert in den We.jahren? Was kann Frau selbst tun, um die We.jahre so gut wie möglich zu erleben? Im Kurs werden natürliche Hilfsmittel besprochen und erklärt, Entspannungstechniken vermittelt , die Psyche gestärkt, sodaß die betroffenen Frauen bei auftretenden We.jahrsproblemen die Möglichkeit haben,sich selbst helfen zu können.

```html
<!DOCTYPE html>
<html lang="de">
<head>
<meta charset="utf-8">
<title>Wechseljahre – Beratung und Begleitung</title>
<link rel="stylesheet" href="https://fonts.googleapis.com/css2?family=Fira+Sans+Condensed:wght@400;500&family=Kalam:wght@400;700&display=swap">
<style>
  :root{
    --red:#d22d51;
    --red-line:#e63b3d;
    --cream:#fbf19e;
    --title-yellow:#f8e866;
    --ink:#2f2f2f;
    --grey-box:#dcdcdc;
    --placeholder:#eef0f8;
    --page:#ffffff;
    --bg:#f2f2f2;
  }
  *{margin:0;padding:0;box-sizing:border-box}
  html,body{width:1200px;height:2543px;overflow:hidden;background:var(--bg)}
  body{position:relative;font-family:"Fira Sans Condensed",sans-serif;color:var(--ink)}
  .panel{position:absolute;left:11px;width:1176px;background:var(--page);overflow:hidden;box-shadow:0 0 4px rgba(0,0,0,.25)}
  .panel--front{top:11px;height:1252px}
  .panel--inside{top:1282px;height:1249px}
  .shapes{position:absolute;left:0;top:0}
  .abs{position:absolute}

  /* front */
  .owner-name{left:40px;top:42px;font-size:32px;font-weight:400}
  .owner-titles{left:40px;top:88px;font-size:22px;line-height:27px;color:#444}
  .placeholder-box{left:40px;top:160px;width:498px;height:265px;background:var(--placeholder)}
  .services{left:40px;top:466px;list-style:none;color:var(--red);font-size:25px}
  .services li{height:76px}
  .services li::before{content:"• ";font-size:18px;vertical-align:3px}
  .headline{left:627px;top:26px;font-family:"Kalam",cursive;font-weight:700;color:var(--title-yellow);font-size:60px;letter-spacing:3px;line-height:1}
  .subline{left:627px;top:94px;font-family:"Kalam",cursive;font-weight:700;color:var(--title-yellow);font-size:30px;letter-spacing:1.5px;line-height:1}
  .topics{left:627px;top:142px;font-family:"Kalam",cursive;color:#fff;font-size:26px;line-height:36px;list-style:none}
  .topics .tight{line-height:29px;padding-top:4px;padding-bottom:3px}
  .quote{left:640px;top:1015px;width:520px;text-align:center;font-family:"Kalam",cursive;color:var(--red);font-size:36px;line-height:66px}
  .brand{left:46px;top:1090px;display:flex;align-items:center;gap:10px}
  .brand-dot{width:22px;height:22px;border-radius:50%;background:var(--ink)}
  .brand-name{font-size:30px;font-weight:500;color:var(--ink);letter-spacing:1px}
  .contact{left:209px;top:1062px;font-size:17px;line-height:21px}
  .contact strong{font-weight:500}
  .contact table{border-collapse:collapse;margin-top:8px}
  .contact td{padding:0 12px 0 0;vertical-align:top}

  /* inside */
  .section-title{left:45px;top:26px;color:#fff;font-size:34px;font-weight:400}
  .intro{left:47px;top:124px;width:496px;font-size:21px;line-height:29px;text-align:justify;hyphens:auto}
  .intro p{margin-bottom:29px}
  .course-box{left:628px;top:73px;width:505px;height:382px;background:var(--grey-box);padding:12px 26px;font-size:21px;line-height:26px}
  .course-box h2{font-weight:400;font-size:28px;line-height:36px;margin-bottom:10px}
  .course-box h3{font-weight:500;font-size:21px;margin-top:10px}
  .course-box .note{margin-top:10px}
  .course-text{left:628px;top:486px;width:505px;font-size:21px;line-height:29px;text-align:justify;hyphens:auto;z-index:2}
  .course-text p{margin-bottom:29px}
  .course-text .lead{margin-bottom:10px}
  .forest-caption{left:620px;top:1116px;width:520px;text-align:center;font-family:"Kalam",cursive;color:#fff;font-size:34px;line-height:34px;text-shadow:0 1px 3px rgba(0,0,0,.4)}
</style>
</head>
<body>

<section class="panel panel--front">
  <svg class="shapes" width="1176" height="1252" viewBox="0 0 1176 1252">
    <defs>
      <linearGradient id="meadow" x1="0" y1="0" x2="0" y2="1">
        <stop offset="0" stop-color="#b9c97a"/>
        <stop offset=".45" stop-color="#8aa653"/>
        <stop offset=".8" stop-color="#9cc03e"/>
        <stop offset="1" stop-color="#d8e88a"/>
      </linearGradient>
    </defs>
    <path d="M588 4 H1176 V325 C1000 332 800 348 588 372 Z" fill="var(--red)"/>
    <path d="M588 372 C800 348 1000 332 1176 325 V345 C1000 350 800 368 588 392 Z" fill="var(--cream)"/>
    <path d="M588 392 C800 368 1000 350 1176 345 V356 C1000 360 800 380 588 404 Z" fill="var(--red-line)"/>
    <path role="img" aria-label="Foto: Frau sitzt lächelnd im Gras vor sonnigen Bäumen" d="M588 404 C800 380 1000 360 1176 356 V930 C1000 940 800 960 588 980 Z" fill="url(#meadow)"/>
    <path d="M0 995 C200 1040 520 1030 1176 918 V1252 H0 Z" fill="var(--cream)"/>
  </svg>

  <h1 class="abs owner-name">Helene Marwitz-Brandt</h1>
  <p class="abs owner-titles">Wechseljahre-Beraterin (zert.)<br>Systemische Beratung (zert.)</p>
  <div class="abs placeholder-box"></div>
  <ul class="abs services">
    <li>Psycholog. Beratung in allen Lebenslagen</li>
    <li>Wechseljahresberatung</li>
    <li>Gesundheits- und Ernährungsberatung</li>
    <li>Fastenbegleitung</li>
    <li>Trauerbegleitung</li>
    <li>Bachblütenberatung</li>
    <li>Klangmassagen</li>
  </ul>

  <div class="abs headline">WECHSELJAHRE</div>
  <div class="abs subline">BERATUNG UND BEGLEITUNG</div>
  <ul class="abs topics">
    <li>Vorbereitung auf die Wechseljahre</li>
    <li>Leben in den Wechseljahren</li>
    <li class="tight">Möglichkeiten der Selbsthilfe<br>bei entsprechenden Beschwerden</li>
    <li>Was kommt danach?</li>
  </ul>

  <div class="abs brand"><span class="brand-dot"></span><span class="brand-name">Lunara</span></div>
  <div class="abs contact">
    <strong>Lunara</strong><br>
    Helene Marwitz-Brandt<br>
    Lindenpad 12<br>
    6411AB Heiderveld / NL
    <table>
      <tr><td>Telefon:</td><td>0241 / 40 27 16 53</td></tr>
      <tr><td>oder</td><td>+31(0)43/ 6 18 29 04</td></tr>
      <tr><td>Mail:</td><td>mondhalmkreise.praxis@postfach.de</td></tr>
    </table>
  </div>
  <p class="abs quote">Alles hat nur die<br>Bedeutung, die man<br>ihr gibt.</p>
</section>

<section class="panel panel--inside">
  <svg class="shapes" width="1176" height="1249" viewBox="0 0 1176 1249">
    <defs>
      <radialGradient id="forest" cx=".5" cy=".55" r=".6">
        <stop offset="0" stop-color="#f6f2a0"/>
        <stop offset=".25" stop-color="#b8cf4e"/>
        <stop offset=".65" stop-color="#5f8f2c"/>
        <stop offset="1" stop-color="#2f5a1e"/>
      </radialGradient>
    </defs>
    <path d="M0 0 H1176 V12 C760 26 380 80 0 98 Z" fill="var(--red)"/>
    <path d="M0 858 C300 872 650 970 1176 920 V936 C650 985 300 892 0 878 Z" fill="var(--cream)"/>
    <path role="img" aria-label="Foto: sonnendurchfluteter Laubwald" d="M0 878 C300 892 650 985 1176 936 V1249 H0 Z" fill="url(#forest)"/>
  </svg>

  <h2 class="abs section-title">Kursangebot Wechseljahre</h2>

  <div class="abs intro">
    <p>Im Alter von Ende 30 bis ca. 60 Jahren erfolgt eine hormonelle Umstellung des weiblichen Körpers- die sog. Wechseljahre.</p>
    <p>Sie bringen körperliche und seelische Veränderungen mit sich, die verunsichern können und von uns Frauen in unterschiedlicher Intensität und Dauer erlebt werden. Viele Fragen ergeben sich und somit auch der Wunsch nach Unterstützung.</p>
    <p>So individuell die Symptome sind, so vielfältig sind auch die Lösungen.</p>
    <p>Gleichzeitig erleben auch viele von uns Einschnitte in ihren Beziehungen, die Kinder gehen aus dem Haus oder es fehlt der Sinn im Arbeitsalltag.</p>
    <p>Es tauchen Fragen auf, wie: Was will ich eigentlich, wie möchte ich mein Leben noch gestalten? Habe ich den Mut und die Kraft etwas zu ändern?</p>
    <p>In solchen Zeiten ist es wichtig, unsere Aufmerksamkeit auf uns selbst und nach Innen zu richten.</p>
  </div>

  <div class="abs course-box">
    <h2>Wechseljahre - Start Kurs 2017</h2>
    <p>11. September - 16. Oktober<br>6 x Montags 19.00 - 20.30 Uhr</p>
    <h3>Kursbeitrag</h3>
    <p>139,-- pro Teilnehmerin</p>
    <h3>Kursort</h3>
    <p>Lindenhof Apotheke - Seminarraum<br>Lindenweg 8<br>52100 Musterrath-Au</p>
    <p class="note">Anmeldung gern in der Lindenhof Apotheke<br>oder telef. in meiner Praxis.</p>
  </div>

  <div class="abs course-text">
    <p class="lead">In diesem 6teiligen Kurs geht es unter anderem um:</p>
    <p>Beginn der Wechseljahre<br>Was passiert in den Wechseljahren? Wie erkennt Frau z.B. psychische Probleme und wie kann sie sich selbst helfen? Was kann Frau tun, um die Wechseljahre so gut wie möglich zu erleben? Leben während der Wechseljahre, und was dann?</p>
    <p>Im Kurs geht es primär um das Verstehen der Wechseljahre mit ihren evtl. auftretenden Problemen. Dadurch besteht die Möglichkeit, nach dem Motto - Problem erkannt, Problem gebannt, - die vermittelten natürlichen Hilfsmittel, Entspannungstechniken, Meditationen etc. nach Bedarf eigenständig einsetzen zu können.</p>
  </div>

  <p class="abs forest-caption">Aufmerksamkeit auf sich selbst<br>und nach Innen</p>
</section>

</body>
</html>
```